Document Processing Services and Solutions for School Systems

I am looking to design a brochure for both Digital and Paper use. I can supply the written content. Would be looking for an overall design of the brochure with provided content worked into it.

```html
<!DOCTYPE html>
<html lang="en">
<head>
<meta charset="utf-8">
<title>Meridian Systems – Document Processing for Schools</title>
<link href="https://fonts.googleapis.com/css2?family=Exo+2:ital,wght@1,800;1,900&family=Montserrat+Alternates:ital,wght@0,500;1,600&display=swap" rel="stylesheet">
<style>
  :root{
    --navy:#2e2f94;
    --gold:#c99a06;
    --ink:#222222;
    --paper:#ffffff;
    --panel:#2f3196;
    --rule:#3f42b0;
  }
  html,body{margin:0;padding:0;overflow:hidden;background:var(--paper);}
  .brochure{position:relative;width:1200px;height:927px;overflow:hidden;background:var(--paper);font-family:"Montserrat Alternates",sans-serif;color:var(--ink);}
  .headline{position:absolute;margin:0;font-family:"Exo 2",sans-serif;font-weight:900;font-style:italic;font-size:42px;line-height:37px;text-transform:uppercase;letter-spacing:.5px;}
  .headline .navy{color:var(--navy);display:block;}
  .headline .gold{color:var(--gold);display:block;}
  .services-title{left:64px;top:50px;}
  .why-title{left:678px;top:52px;}
  .brand{position:absolute;font-family:"Montserrat Alternates",sans-serif;font-weight:500;font-size:15px;color:var(--navy);display:flex;align-items:center;gap:6px;white-space:nowrap;}
  .brand::before{content:"";width:9px;height:9px;background:var(--gold);}
  .brand-left{left:400px;top:74px;}
  .brand-right{left:1006px;top:74px;}

  .service{position:absolute;left:0;width:560px;height:212px;}
  .service .rule{position:absolute;left:0;width:450px;height:2px;background:var(--gold);}
  .service .rule.top{top:0}
  .service .rule.bottom{bottom:0}
  .service .photo{position:absolute;left:341px;top:-2px;width:212px;height:212px;border-radius:50%;border:3px solid var(--gold);box-sizing:border-box;}
  .service .icon{position:absolute;left:57px;top:14px;width:54px;height:54px;}
  .service h2{position:absolute;left:127px;top:13px;margin:0;font-family:"Exo 2",sans-serif;font-weight:900;font-style:italic;font-size:21px;line-height:18px;color:var(--navy);text-transform:uppercase;}
  .service ul{position:absolute;left:57px;top:82px;margin:0;padding:0;list-style:none;width:280px;}
  .service li{position:relative;padding-left:15px;font-size:11.6px;line-height:14.6px;margin-bottom:14.5px;font-weight:500;}
  .service li svg{position:absolute;left:0;top:4px;width:9px;height:9px;}
  .scan{top:154px}
  .cloud{top:402px}
  .workflow{top:652px}
  .workflow ul{top:100px}
  .photo-scan{background:radial-gradient(circle at 40% 45%,#e9e6e3,#b9b2ac 55%,#6a5f58);}
  .photo-cloud{background:radial-gradient(circle at 60% 45%,#4d6e9a,#1c2433 50%,#0a0c12 80%);}
  .photo-office{background:linear-gradient(180deg,#d8d2cb,#8f6f5c 55%,#3a3a40);}

  .benefits-panel{position:absolute;left:680px;top:203px;width:520px;height:575px;background:var(--panel);border-radius:24px 0 0 24px;}
  .divider{position:absolute;left:744px;width:236px;height:2px;background:var(--rule);}
  .portrait{position:absolute;left:900px;top:330px;width:300px;height:597px;
    clip-path:polygon(95px 0,300px 0,300px 597px,8px 597px,8px 385px,38px 215px,62px 60px);
    background:linear-gradient(180deg,#e8d09a 0%,#f3efe9 30%,#ececec 58%,#35b9c9 76%,#e6673f 90%,#1d1d1d 100%);}
  .benefit{position:absolute;left:648px;width:340px;}
  .benefit .badge{position:absolute;left:0;top:0;width:76px;height:76px;}
  .benefit h3{position:absolute;left:95px;top:3px;margin:0;font-weight:600;font-style:italic;font-size:21px;color:var(--gold);white-space:nowrap;}
  .benefit p{position:absolute;left:96px;top:34px;margin:0;font-size:13.4px;line-height:18.3px;color:#fff;font-weight:500;white-space:nowrap;}
  .b1{top:252px}.b2{top:380px}.b3{top:509px}.b4{top:630px}
  .site{position:absolute;left:680px;top:828px;font-size:19px;font-weight:500;color:var(--ink);letter-spacing:.3px;}
</style>
</head>
<body>
<main class="brochure">
  <h1 class="headline services-title"><span class="navy">Our</span><span class="gold">Services</span></h1>
  <div class="brand brand-left">Meridian Systems Inc</div>

  <section class="service scan">
    <span class="rule top"></span><span class="rule bottom"></span>
    <svg class="icon" viewBox="0 0 54 54"><circle cx="27" cy="27" r="25.5" fill="var(--navy)" stroke="var(--gold)" stroke-width="3"/><g fill="none" stroke="#fff" stroke-width="1.8"><path d="M15 20v-5h5M34 15h5v5M39 34v5h-5M20 39h-5v-5"/><rect x="20" y="18" width="14" height="18" rx="1.5"/><path d="M16 27h22"/></g></svg>
    <h2>Document<br>Scanning<br>&amp; Conversion</h2>
    <ul>
      <li><svg viewBox="0 0 10 10"><circle cx="5" cy="5" r="4.2" fill="none" stroke="var(--gold)"/><path d="M3 5l1.5 1.5L7 4" fill="none" stroke="var(--gold)"/></svg>Convert paper records into digital formats for easy access and storage.</li>
      <li><svg viewBox="0 0 10 10"><circle cx="5" cy="5" r="4.2" fill="none" stroke="var(--gold)"/><path d="M3 5l1.5 1.5L7 4" fill="none" stroke="var(--gold)"/></svg>High-speed scanning for student records, administrative files, and historical archives.</li>
      <li><svg viewBox="0 0 10 10"><circle cx="5" cy="5" r="4.2" fill="none" stroke="var(--gold)"/><path d="M3 5l1.5 1.5L7 4" fill="none" stroke="var(--gold)"/></svg>OCR (Optical Character Recognition) for searchable and editable documents.</li>
    </ul>
    <div class="photo photo-scan" role="img" aria-label="Staff member feeding paper records into a high-speed document scanner"></div>
  </section>

  <section class="service cloud">
    <span class="rule top"></span><span class="rule bottom"></span>
    <svg class="icon" viewBox="0 0 54 54"><circle cx="27" cy="27" r="25.5" fill="var(--navy)" stroke="var(--gold)" stroke-width="3"/><g fill="none" stroke="#fff" stroke-width="1.8"><path d="M18 30a5 5 0 0 1 1-10 8 8 0 0 1 15-1 5.5 5.5 0 0 1 2 11z"/><path d="M21 30v6M27 30v8M33 30v6"/><circle cx="21" cy="37.5" r="1.5"/><circle cx="27" cy="39.5" r="1.5"/><circle cx="33" cy="37.5" r="1.5"/></g></svg>
    <h2>Cloud-Based<br>Document<br>Management</h2>
    <ul>
      <li><svg viewBox="0 0 10 10"><circle cx="5" cy="5" r="4.2" fill="none" stroke="var(--gold)"/><path d="M3 5l1.5 1.5L7 4" fill="none" stroke="var(--gold)"/></svg>Secure, centralized document storage accessible from anywhere.</li>
      <li><svg viewBox="0 0 10 10"><circle cx="5" cy="5" r="4.2" fill="none" stroke="var(--gold)"/><path d="M3 5l1.5 1.5L7 4" fill="none" stroke="var(--gold)"/></svg>Role-based access controls for administrators, teachers, and staff.</li>
      <li><svg viewBox="0 0 10 10"><circle cx="5" cy="5" r="4.2" fill="none" stroke="var(--gold)"/><path d="M3 5l1.5 1.5L7 4" fill="none" stroke="var(--gold)"/></svg>Automated backups and compliance with educational data security standards.</li>
    </ul>
    <div class="photo photo-cloud" role="img" aria-label="Hand touching a glowing cloud storage symbol linked to folders"></div>
  </section>

  <section class="service workflow">
    <span class="rule top"></span><span class="rule bottom"></span>
    <svg class="icon" viewBox="0 0 54 54"><circle cx="27" cy="27" r="25.5" fill="var(--navy)" stroke="var(--gold)" stroke-width="3"/><g fill="none" stroke="#fff" stroke-width="1.8"><circle cx="27" cy="27" r="13" stroke-dasharray="6 3"/><circle cx="27" cy="27" r="7"/><path d="M25 24l5 3-5 3z" fill="#fff"/></g></svg>
    <h2>Workflow<br>Automation</h2>
    <ul>
      <li><svg viewBox="0 0 10 10"><circle cx="5" cy="5" r="4.2" fill="none" stroke="var(--gold)"/><path d="M3 5l1.5 1.5L7 4" fill="none" stroke="var(--gold)"/></svg>Digitize and streamline approval processes for enrollment, transcripts, and HR forms.</li>
      <li><svg viewBox="0 0 10 10"><circle cx="5" cy="5" r="4.2" fill="none" stroke="var(--gold)"/><path d="M3 5l1.5 1.5L7 4" fill="none" stroke="var(--gold)"/></svg>Reduce paperwork and improve efficiency with automated workflows.</li>
      <li><svg viewBox="0 0 10 10"><circle cx="5" cy="5" r="4.2" fill="none" stroke="var(--gold)"/><path d="M3 5l1.5 1.5L7 4" fill="none" stroke="var(--gold)"/></svg>Integration capable with existing school management systems.</li>
    </ul>
    <div class="photo photo-office" role="img" aria-label="Bright open-plan office with brick walls, desks and computers"></div>
  </section>

  <h1 class="headline why-title"><span class="navy">Why</span><span class="gold">Choose<br>Us?</span></h1>
  <div class="brand brand-right">Meridian Systems Inc</div>

  <div class="benefits-panel"></div>
  <span class="divider" style="top:350px"></span>
  <span class="divider" style="top:483px"></span>
  <span class="divider" style="top:607px"></span>
  <div class="portrait" role="img" aria-label="Staff member in glasses holding a stack of colourful ring binders"></div>

  <div class="benefit b1">
    <svg class="badge" viewBox="0 0 76 76"><circle cx="38" cy="38" r="36" fill="var(--gold)" stroke="var(--navy)" stroke-width="3"/><g fill="none" stroke="#fff" stroke-width="2"><circle cx="24" cy="46" r="9"/><path d="M24 41v5h4"/><path d="M36 52V38M42 52V32M48 52V26M30 30l8-7 5 4 8-9M47 18h4v4"/></g></svg>
    <h3>Increased Efficiency</h3>
    <p>Save time with digital workflows<br>and instant document retrieval.</p>
  </div>
  <div class="benefit b2">
    <svg class="badge" viewBox="0 0 76 76"><circle cx="38" cy="38" r="36" fill="var(--gold)" stroke="var(--navy)" stroke-width="3"/><g fill="none" stroke="#fff" stroke-width="2"><path d="M36 18l14 5v11c0 10-6 16-14 20-8-4-14-10-14-20V23z"/><path d="M30 34h4v10h-4zM34 43h8c2 0 3-1 3-3l1-5c0-2-1-3-3-3h-4l1-4c0-2-3-2-3 0l-3 5"/><path d="M52 16v6M50 18l2-2 2 2M57 20v5M55 22l2-2 2 2"/></g></svg>
    <h3>Enhanced Security</h3>
    <p>Protect sensitive student<br>&amp;faculty information.</p>
  </div>
  <div class="benefit b3">
    <svg class="badge" viewBox="0 0 76 76"><circle cx="38" cy="38" r="36" fill="var(--gold)" stroke="var(--navy)" stroke-width="3"/><g fill="none" stroke="#fff" stroke-width="2"><path d="M34 19h8l-2 5c7 3 10 8 10 13 0 5-5 7-12 7s-12-2-12-7c0-5 3-10 10-13z"/><path d="M41 29c-2-1-5-1-5 1.5s5 1.5 5 4-3 2.5-5 1.5M38 27v12"/><path d="M18 50l7-6c2-1 4-1 6 0h8c2 0 2 3 0 3h-7M31 52h12l9-7c2-1 4 1 2 3l-9 8H28l-4 3"/></g></svg>
    <h3>Cost Savings</h3>
    <p>Reduce paper, printing,<br>and storage costs.</p>
  </div>
  <div class="benefit b4">
    <svg class="badge" viewBox="0 0 76 76"><circle cx="38" cy="38" r="36" fill="var(--gold)" stroke="var(--navy)" stroke-width="3"/><g fill="none" stroke="#fff" stroke-width="2"><circle cx="40" cy="36" r="11"/><path d="M40 25v-5M40 20c-3-3-7-3-9-1 3 2 6 2 9 1zM40 20c3-3 7-3 9-1-3 2-6 2-9 1z"/><path d="M18 52l7-6c2-1 4-1 6 0h8c2 0 2 3 0 3h-7M31 54h12l9-7c2-1 4 1 2 3l-9 8H28l-4 3"/></g></svg>
    <h3>Eco-Friendly</h3>
    <p>Minimize your school’s<br>carbon footprint by<br>going digital.</p>
  </div>

  <div class="site">www.meridiansys.com</div>
</main>
</body>
</html>
```